Professional, Elegant, Modern and Playful business card Design for an Orthodontist (Dentist)

We need a new business card design for an Orthodontist (Dentist).
We would like to see designs that are elegant, but also playful. The designs and colors should be in harmony with the existing logo (uploaded).
Size: standard size (85mm x 55mm)
The font of the logo text is roboto (Plexora), you don't need to use the same font, but the used font has to be in harmony with the font used in the logo.
The colors used have to be in harmony with the logo.

Target Market(s)

Orthodontist (Dentist)

Industry/Entity Type

Dental Clinic

Contact Information for Business Card

* Size: standard size (85mm x 55mm)
* The font of the logo text is roboto (Plexora), you don't need to use the same font, but the used font has to be in harmony with the font used in the logo.
* The colors used have to be in harmony with the logo.

* Following Information have to be on the front side:
- Logo with company name (see uploaded files) as a unit
or
- separate the logo from the text and position them separately
- Text that has to be on the front side:
Kieferorthopädie Brunnhalde
Dr. med. dent. Davor Lesnik
Fachzahnarzt für Kieferorthopädie (CH)
(if there is enough space, please also write:
Eidg. dipl. Zahnarzt, Mitglied VFT und BZP)
(address:)
Wendelhofweg 7
8634 Ferwangen
(telephone number:)
044 619 27 40
(if there is much space left, also fax number, but it is not mandatory:
044 619 27 41)
info@spangenhof.net
www.spangenhof.net
(If there is space left:
QR-code with the homepage-adress: www.spangenhof.net
and in the center of the QR-Code a little logo)
- It is important not to overload the front side. Put in the optional parts on the front side only if it doesn't look overloaded.

* Following Information have to be on the back side:
- An abstract map sketch (freehand drawing) of the location of the office is uploaded (Map on the back side of the business card.pdf). Please do a nicely designed abstract map based on this sketch.
- Feel free to change everything to make it good.
- For better reading the text has been rewritten in the sketch on the outside of the border of the card.
- You can see the original situation e.g. in plexora maps (Address: Wendelhofweg 7, 8634 Ferwangen, Switzerland)
- Marked as yellow are the important streets. These should not be yellow in the final design.
- The symbols of the freeway (green symbol) and the car park are uploaded ad vector graphics.
- "A1" should be the same green color as the background of the freeway (green symbol).
- The symbols of the bus stops and the railway station are uploaded as pixel graphics. Please convert them to vector graphics and make the background blue the same.
- The badges of the train numbers (S3 and S12) and bus numbers (31, 302, 303, 307, 308) are also pixel graphics. Please draw them as vector graphics. The font doesn't have to be identical with the one in the sketch, but the color codes need to be the same in the final design.
- The dashed blue line is a footway only. It should not be drawn like this in the final design. The design decision is up to you, but it should be different from the streets.
- The building of the office and the arrow showing the entrance should be clearly
visible and distinguishable form the other drawings.

Font styles to use
Sans Serif

Colors

Designer to choose colors to be used in the design.

Requirements
Must have
• - vector graphics
• - vector files: adobe illustrator or compatible
Should not have
• - pixel graphics

```html
<!DOCTYPE html>
<html lang="de">
<head>
<meta charset="utf-8">
<title>Kieferorthopädie Brunnhalde – Visitenkarte</title>
<link rel="stylesheet" href="https://fonts.googleapis.com/css2?family=Comfortaa:wght@500;600&family=Roboto:ital,wght@1,400;1,700&display=swap">
<style>
  :root {
    --navy: #201d5e;
    --sky: #27a3dc;
    --paper: #eeeeee;
    --white: #ffffff;
    --ink-grey: #555a66;
    --map-grey: #c9c9cc;
    --map-road: #b9ab9c;
    --stage: #6a6a6c;
  }
  * { box-sizing: border-box; margin: 0; padding: 0; }
  html, body { width: 1200px; height: 675px; overflow: hidden; }
  body {
    background: var(--stage);
    position: relative;
    font-family: "Comfortaa", sans-serif;
  }
  .card {
    position: absolute;
    top: 162px;
    width: 540px;
    height: 350px;
    background: var(--navy);
    overflow: hidden;
  }
  .card--front { left: 40px; }
  .card--back { left: 620px; }
  .card__shapes { position: absolute; inset: 0; }

  .brand {
    position: absolute;
    left: 40px;
    top: 150px;
    width: 260px;
    text-align: center;
  }
  .brand__dot {
    width: 44px; height: 44px; border-radius: 50%;
    background: var(--navy);
    margin: 0 auto 24px;
  }
  .brand__name {
    font-family: "Roboto", sans-serif;
    font-style: italic;
    font-weight: 700;
    font-size: 18px;
    color: var(--navy);
    white-space: nowrap;
  }
  .brand__person, .brand__title {
    font-family: "Roboto", sans-serif;
    font-style: italic;
    font-weight: 400;
    font-size: 11.5px;
    color: var(--ink-grey);
    letter-spacing: 0.4px;
    line-height: 1.25;
    text-align: left;
    padding-left: 4px;
  }
  .brand__person { margin-top: 4px; }

  .contact {
    position: absolute;
    height: 22px;
    background: var(--white);
    border-radius: 11px;
    color: var(--navy);
    font-size: 13.5px;
    font-weight: 600;
    line-height: 22px;
    text-align: right;
    padding-right: 8px;
    white-space: nowrap;
  }
  .contact__icon {
    position: absolute;
    left: -6px; top: -3px;
    width: 28px; height: 28px;
    border-radius: 50%;
    background: #bfe3f5;
    border: 2px solid var(--sky);
  }
  .contact__icon svg { position: absolute; left: 5px; top: 5px; width: 14px; height: 14px; }
  .contact--address { left: 232px; top: 87px; width: 270px; }
  .contact--phone   { left: 276px; top: 139px; width: 224px; }
  .contact--web     { left: 302px; top: 195px; width: 195px; }
  .contact--mail    { left: 313px; top: 259px; width: 181px; }

  .map {
    position: absolute;
    left: 38px; top: 32px;
    width: 454px; height: 280px;
    border: 5px solid var(--white);
    background: linear-gradient(135deg, var(--map-grey), #d8d4cf 55%, var(--map-road));
  }
</style>
</head>
<body>

  <section class="card card--front" aria-label="Vorderseite">
    <svg class="card__shapes" viewBox="0 0 540 350" aria-hidden="true">
      <path d="M0,0 L70,0 C250,15 385,150 395,350 L350,350 C335,165 190,45 0,38 Z" fill="var(--sky)"/>
      <path d="M0,38 C190,45 335,165 350,350 L0,350 Z" fill="var(--paper)"/>
    </svg>

    <div class="brand">
      <div class="brand__dot"></div>
      <div class="brand__name">Kieferorthopädie Brunnhalde</div>
      <div class="brand__person">Dr. med. dent. Davor Lesnik</div>
      <div class="brand__title">Fachzahnarzt für Kieferorthopädie (CH)</div>
    </div>

    <div class="contact contact--address">
      <span class="contact__icon"><svg viewBox="0 0 14 14"><path d="M1 7 L7 2 L13 7 M3 6 V12 H11 V6" fill="none" stroke="var(--navy)" stroke-width="1.8"/></svg></span>
      Wendelhofweg 7 - 8634 Ferwangen
    </div>
    <div class="contact contact--phone">
      <span class="contact__icon"><svg viewBox="0 0 14 14"><rect x="4" y="1" width="6" height="12" rx="1.5" fill="var(--navy)"/><rect x="5.2" y="3" width="3.6" height="5" fill="#bfe3f5"/></svg></span>
      044 619 27 40
    </div>
    <div class="contact contact--web">
      <span class="contact__icon"><svg viewBox="0 0 14 14"><circle cx="7" cy="7" r="5.5" fill="none" stroke="var(--navy)" stroke-width="1.5"/><path d="M1.5 7 H12.5 M7 1.5 C4 4 4 10 7 12.5 C10 10 10 4 7 1.5" fill="none" stroke="var(--navy)" stroke-width="1.2"/></svg></span>
      www.spangenhof.net
    </div>
    <div class="contact contact--mail">
      <span class="contact__icon"><svg viewBox="0 0 14 14"><rect x="1" y="3" width="12" height="8" fill="none" stroke="var(--navy)" stroke-width="1.5"/><path d="M1 3 L7 8 L13 3" fill="none" stroke="var(--navy)" stroke-width="1.5"/></svg></span>
      info@spangenhof.net
    </div>
  </section>

  <section class="card card--back" aria-label="Rückseite">
    <svg class="card__shapes" viewBox="0 0 540 350" aria-hidden="true">
      <path d="M300,0 L345,0 C300,120 275,230 300,350 L255,350 C235,230 255,120 300,0 Z" fill="var(--sky)"/>
    </svg>
    <div class="map" role="img" aria-label="Lageplan der Praxis mit Strassen, Bus- und S-Bahn-Haltestellen, Parkhaus, Autobahnanschluss und markiertem Eingang"></div>
  </section>

</body>
</html>
```